Project Managers Business card design

We need business cards for our Project Managers based in Sydney for our business name Korbet Pty Ltd. We project manage property improvements and infrastructure Assets. We provide asset owners Project Management services from original concept, management of architectural and engineering designs, call and select construction tenders, and manage the Asset operational life cycle to conclusion and removal. We are experienced in feasibility studies, risk assessments, quality control, safety control, environmental analysis. We are specialist in Aged Care and Child Care Services. We can provide asset reviewing checklists, asset inspections, contract cost and contract assessments, dispute resolution services and articles and books on safely working and living in environments subject to analysis. the design colours should be queensland marone and NSW sky blue.

Industry/Entity Type

Construction

Contact Information for Business Card

Dennis Marlow (Mb 0402 781954), Gavin Trelford (Mb 0438 216 047), Len Obradin,(Mb 0427 863 105)
E: all business cards: korbet@mailnest.example
Office phone number (02) 9482 3061
Address
Level 1 Harwell Building
47 Fenwick Street, Parramatta
Web: projectmanagers@estateleadsbykorbet.example (to be checked on Printwell web draft)

```html
<!DOCTYPE html>
<html lang="en">
<head>
<meta charset="utf-8">
<title>Korbet Pty Ltd — Business Card</title>
<link rel="stylesheet" href="https://fonts.googleapis.com/css2?family=Arimo:wght@400&family=Cormorant+Garamond:wght@500;600&display=swap">
<style>
  :root {
    --stage: #e9e6e1;
    --paper: #ffffff;
    --ink: #1c1c1c;
    --ink-soft: #3a3a3a;
    --band-black: #0e0e0e;
    --crimson: #cc2443;
    --crimson-deep: #a8172f;
    --white: #ffffff;
  }
  * { margin: 0; padding: 0; box-sizing: border-box; }
  html, body { width: 1200px; height: 858px; overflow: hidden; }
  body {
    background: var(--stage);
    display: flex;
    align-items: center;
    justify-content: center;
    gap: 40px;
    font-family: "Arimo", Arial, sans-serif;
  }
  .card {
    position: relative;
    width: 540px;
    height: 309px;
    overflow: hidden;
    box-shadow: 0 10px 28px rgba(0,0,0,0.18);
  }

  /* Front */
  .card-front { background: var(--paper); }
  .card-front .band { position: absolute; inset: 0; }
  .holder {
    position: absolute;
    left: 58px;
    top: 70px;
  }
  .holder-name {
    font-family: "Cormorant Garamond", "Times New Roman", serif;
    font-weight: 600;
    font-variant: small-caps;
    font-size: 25px;
    letter-spacing: 0.5px;
    color: var(--ink);
    line-height: 1;
  }
  .holder-role {
    font-size: 14px;
    color: var(--ink);
    margin-top: 3px;
  }
  .contact-list {
    position: absolute;
    left: 96px;
    top: 138px;
    list-style: none;
  }
  .contact-list li {
    display: flex;
    align-items: center;
    gap: 9px;
    font-size: 13.5px;
    color: var(--ink-soft);
    line-height: 21px;
  }
  .contact-list svg { width: 11px; height: 11px; fill: var(--ink-soft); flex: none; }
  .office-phone {
    position: absolute;
    right: 22px;
    top: 242px;
    display: flex;
    align-items: center;
    gap: 18px;
    font-size: 17px;
    color: var(--white);
  }
  .office-phone svg { width: 13px; height: 13px; fill: var(--white); }
  .email-tab {
    position: absolute;
    left: 22px;
    top: 254px;
    display: flex;
    align-items: center;
    gap: 10px;
    font-size: 15px;
    color: var(--white);
  }
  .email-tab svg { width: 13px; height: 10px; fill: var(--white); }

  /* Back */
  .card-back {
    background: radial-gradient(ellipse at 55% 40%, var(--crimson) 0%, var(--crimson) 45%, var(--crimson-deep) 100%);
  }
  .back-name {
    position: absolute;
    left: 0; right: 0;
    top: 130px;
    text-align: center;
    font-family: "Cormorant Garamond", "Times New Roman", serif;
    font-weight: 500;
    font-variant: small-caps;
    font-size: 30px;
    letter-spacing: 1px;
    color: var(--white);
  }
  .back-web {
    position: absolute;
    left: 26px;
    bottom: 22px;
    font-size: 14px;
    color: var(--white);
  }
</style>
</head>
<body>

  <section class="card card-front" aria-label="Card front">
    <svg class="band" viewBox="0 0 540 309" aria-hidden="true">
      <polygon points="232,200 540,200 540,309 232,309" fill="var(--band-black)"/>
      <line x1="0" y1="211" x2="250" y2="211" stroke="var(--band-black)" stroke-width="2"/>
      <polygon points="0,218 252,218 284,309 0,309" fill="var(--crimson)" stroke="var(--white)" stroke-width="3"/>
    </svg>

    <div class="holder">
      <p class="holder-name">Gavin Trelford</p>
      <p class="holder-role">projectmanager</p>
    </div>

    <ul class="contact-list">
      <li>
        <svg viewBox="0 0 12 12"><path d="M3 0h6a1 1 0 0 1 1 1v10a1 1 0 0 1-1 1H3a1 1 0 0 1-1-1V1a1 1 0 0 1 1-1zm0 1.5v8h6v-8z"/></svg>
        0438 216 047
      </li>
      <li>
        <svg viewBox="0 0 12 12"><path d="M6 0a6 6 0 1 0 0 12A6 6 0 0 0 6 0zm0 1.2c.8 0 1.6 1.5 1.8 3.6H4.2C4.4 2.7 5.2 1.2 6 1.2zM1.3 5.9h2.8c0 .1 0 .2 0 .3H1.3zm0 .9h2.9c.2 2.1 1 3.9 1.8 4A4.8 4.8 0 0 1 1.3 6.8zm6.5 0h2.9a4.8 4.8 0 0 1-4.7 4c.8-.1 1.6-1.9 1.8-4zm0-.9V5.8h2.9v.1z"/></svg>
        estateleadsbykorbet.example
      </li>
      <li>
        <svg viewBox="0 0 12 12"><path d="M6 0l6 5.5h-1.8V12H7.6V8.2H4.4V12H1.8V5.5H0z"/></svg>
        Level 1 Harwell Building 47 Fenwick Street, Parramatta
      </li>
    </ul>

    <p class="office-phone">
      (02) 9482 3061
      <svg viewBox="0 0 12 12"><path d="M2.4 0.4l2 2.2-1 1.4c.8 1.7 2 2.9 3.6 3.7l1.4-1 2.2 2-1.1 2.2C5.3 10.6 1.4 6.7 0.2 1.5z"/></svg>
    </p>

    <p class="email-tab">
      <svg viewBox="0 0 13 10"><path d="M0 0h13L6.5 5zM0 1.4l6.5 5 6.5-5V10H0z"/></svg>
      korbet@mailnest.example
    </p>
  </section>

  <section class="card card-back" aria-label="Card back">
    <p class="back-name">Gavin Trelford</p>
    <p class="back-web">projectmanagers@estateleadsbykorbet.example</p>
  </section>

</body>
</html>
```